Website Design for two swimming school brands

Looking for a modern, engaging website design for my new business Every Stroke Water Learning. Within that business I have two current brands:
Every Stroke Swim and Yard Paddle
My current website (www.yardpaddle.net) has most of the info you'll need. Feel free to also use my socials for content.
Looking for someone to do the initial design/setup and then hand over full control to me with no ongoing fees or charges (except for hosting), and I'm responsible for all future changes. Ideally made and then can be edited in google sites but open to other options.

Website requirements are quite simple for both pages.
For the Yard Paddle page, I'd like the same info and features that are on my current website presented in a fresh way.
For the Every Stroke page, I'd like to see your concepts for design and possible sections, but it'll be roughly the same as the yard paddle one. I will upload a document soon for text and sections and other information to go on the Every stroke swim page.

For clarity the difference between the business' is one goes out to people's home pools and the other hires out lane space in public pool to conduct lessons.
I'd like a lighter theme for the Yard Paddle Website and a Darker one for the Every Stroke.
Both pages needs to be accessible with picture descriptions for screen reader and other similar features.

I currently use Bookora for all my inquiry, booking and payment functions so the website would need to be compatible with their widgets.

Have a look at the MockUp v2 or the business card design to get the concept of two different brandings working together.

Some text from the Every Stroke Swim Page can be found in this document:
https://docs.example-files.net/document/d/7QpaLmRvXc2TnWb8KdYs4FgHe9JuZoNi3VcXaBt/edit?usp=sharing
-
Feel free to ask any further questions.
Updates

Target Market(s)

Families and disability service providers

Industry/Entity Type

Sports and Recreation

Coding

Coded - Design and coding required

Number of Pages Required

4 page

Requirements
Must have
• Engaging design, ability to put in widgets into website, cross links between two business
Nice to have
• Common elements across the two pages but also points of difference

```html
<!DOCTYPE html>
<html lang="en">
<head>
<meta charset="utf-8">
<title>Yard Paddle – Home Swimming Lessons</title>
<link rel="stylesheet" href="https://fonts.googleapis.com/css2?family=Roboto:wght@400;500;700&display=swap">
<style>
:root{
  --teal:#17a493;
  --teal-dark:#0f8b7d;
  --blue:#1a86c9;
  --cyan:#5fcfd2;
  --ink:#222;
  --muted:#444;
  --footer:#121212;
  --white:#fff;
}
*{box-sizing:border-box;margin:0;padding:0}
html,body{width:1200px;height:4213px;overflow:hidden}
body{position:relative;font-family:"Roboto",Arial,sans-serif;color:var(--ink);background:var(--white)}
.abs{position:absolute}
a{color:inherit;text-decoration:none}

/* Header */
.site-header{position:absolute;left:0;top:0;width:1200px;height:82px;background:var(--white);z-index:5}
.brand-badge{position:absolute;left:102px;top:-58px;width:196px;height:196px;border-radius:50%;background:var(--white);z-index:6;display:flex;align-items:flex-end;justify-content:center;padding-bottom:92px}
.brand-name{font-family:"Roboto",Arial,sans-serif;font-weight:700;font-size:25px;color:var(--teal);letter-spacing:.5px}
.main-nav{position:absolute;top:32px;left:0;font-size:14px;font-weight:400;color:#333}
.main-nav a{position:absolute;white-space:nowrap;text-transform:uppercase}
.main-nav .current{color:var(--teal)}
.search-btn{position:absolute;left:890px;top:24px;width:34px;height:34px;border-radius:50%;background:#eee;display:flex;align-items:center;justify-content:center}
.contact-btn{position:absolute;left:961px;top:20px;width:134px;height:42px;background:var(--teal);color:#fff;font-weight:700;font-size:14px;display:flex;align-items:center;justify-content:center;border-radius:2px}

/* Hero */
.hero{position:absolute;left:0;top:82px;width:1200px;height:690px;background:linear-gradient(100deg,#2aa3b3 0%,#2393a8 45%,#1c7f98 100%)}
.hero-photo{position:absolute;inset:0;background:radial-gradient(ellipse 360px 300px at 870px 250px,rgba(240,220,205,.35),transparent 70%)}
.hero-text{position:absolute;left:111px;top:215px;color:#fff}
.hero-kicker{font-size:36px;font-weight:700}
.hero-title{font-size:74px;font-weight:700;line-height:1;margin-top:10px;letter-spacing:.5px}
.hero-lede{font-size:12.5px;line-height:21px;width:420px;margin-top:18px}
.btn-outline{position:absolute;left:111px;top:510px;width:164px;height:51px;border:2px solid #9fe0c9;background:var(--teal);color:#fff;font-weight:700;font-size:14px;display:flex;align-items:center;justify-content:center;gap:10px}
.btn{display:inline-flex;align-items:center;gap:12px;color:#fff;font-weight:700;font-size:14px;justify-content:center}

/* Audience */
.section-title{font-weight:700;font-size:31px;color:#222;text-align:center;line-height:36px}
.rule{width:56px;height:4px;background:var(--teal);border-radius:2px}
.audience-circle{position:absolute;border-radius:50%;background:var(--teal);color:#fff;display:flex;flex-direction:column;align-items:center;justify-content:center;text-align:center;font-weight:700;font-size:21px;line-height:24px}
.audience-photo{position:absolute;left:417px;top:942px;width:372px;height:372px;border-radius:50%;border:6px solid #fff;background:linear-gradient(160deg,#5bc3ea 0%,#2e9bd6 55%,#1f7fbf 100%);display:flex;align-items:flex-end;justify-content:center;padding-bottom:92px;color:#fff;font-weight:700;font-size:20px;z-index:2}

/* About */
.about-bg{position:absolute;left:0;top:1330px;width:1200px;height:620px;background:linear-gradient(180deg,#fff 0%,#eef6fa 35%,#bcd9e8 55%,#4e97bb 72%,#2c7aa4 100%)}
.about-photo{position:absolute;left:126px;top:1395px;width:400px;height:456px;border-radius:14px;background:linear-gradient(150deg,#3b7fb8 0%,#6c8a9b 45%,#b9c3c9 100%);z-index:2}
.about-bar{position:absolute;left:500px;top:1422px;width:56px;height:400px;background:var(--teal);border-radius:0 12px 12px 0}
.h2{font-size:31px;font-weight:700;color:#222}
.body-copy{font-size:15px;line-height:26px;color:var(--muted);text-align:justify}
.btn-blue{position:absolute;background:var(--blue);height:48px;border-radius:2px}

/* Locations */
.check-list{list-style:none;font-size:14.5px;color:#333;line-height:25px}
.check-list li{position:absolute;left:0;padding-left:31px;width:440px}
.check-list li svg{position:absolute;left:0;top:6px}
.dot-grid{position:absolute;left:694px;top:2062px;width:76px;height:62px;background-image:radial-gradient(circle,#1fb59f 1.4px,transparent 1.6px);background-size:11px 11px}

/* Why */
.why-band{position:absolute;left:0;top:2500px;width:1200px;height:680px;background:linear-gradient(180deg,#62cfd3 0%,#4cc3ca 50%,#38b3be 100%)}
.why-feature{position:absolute;width:220px;text-align:center;color:#fff;font-weight:700;font-size:14.5px;line-height:26px}
.why-icon{width:102px;height:102px;border:3px solid #fff;border-radius:50%;margin:0 auto 26px;display:flex;align-items:center;justify-content:center}

/* Footer */
.site-footer{position:absolute;left:0;top:3780px;width:1200px;height:373px;background:var(--footer);color:#fff}
.foot-h{position:absolute;font-size:15px;font-weight:700}
.foot-links a{position:absolute;font-size:14.5px}
.contact-row{position:absolute;display:flex;align-items:center;gap:16px;font-size:14.5px}
.contact-ico{width:26px;height:26px;border-radius:50%;background:#3a3a3a;display:flex;align-items:center;justify-content:center}
.social{position:absolute;width:31px;height:31px;border-radius:50%;border:2px solid #fff}
.legal-bar{position:absolute;left:0;top:4153px;width:1200px;height:60px;background:var(--teal);color:#fff;font-size:13px}
</style>
</head>
<body>

<header class="site-header">
  <div class="brand-badge"><span class="brand-name">YARDPADDLE</span></div>
  <nav class="main-nav" aria-label="Main">
    <a class="current" style="left:330px">Home</a>
    <a style="left:396px">About me</a>
    <a style="left:495px">My services</a>
    <a style="left:613px">Testimonies</a>
    <a style="left:732px">Pricing</a>
    <a style="left:816px">Links</a>
  </nav>
  <span class="search-btn" aria-label="Search">
    <svg width="14" height="14" viewBox="0 0 14 14"><circle cx="6" cy="6" r="4.3" fill="none" stroke="#222" stroke-width="2"/><line x1="9.2" y1="9.2" x2="13" y2="13" stroke="#222" stroke-width="2"/></svg>
  </span>
  <a class="contact-btn">CONTACT US</a>
</header>

<section class="hero">
  <div class="hero-photo" role="img" aria-label="Smiling older woman swimming with a blue kickboard in a turquoise pool"></div>
  <div class="hero-text">
    <div class="hero-kicker">Welcome To</div>
    <h1 class="hero-title">Yard Paddle</h1>
    <p class="hero-lede">Yard Paddle offers a personalised approach to swimming lessons that can help individuals overcome their fears and technical challenges.</p>
  </div>
  <a class="btn-outline" style="top:428px">GET STARTED
    <svg width="14" height="14" viewBox="0 0 14 14"><circle cx="7" cy="7" r="7" fill="#fff"/><path d="M4 7h5M7 4.5L9.5 7 7 9.5" stroke="#17a493" stroke-width="1.8" fill="none"/></svg>
  </a>
</section>
<svg class="abs" style="left:0;top:700px" width="1200" height="80" viewBox="0 0 1200 80" aria-hidden="true">
  <path d="M0,36 L30,48 L55,40 L90,54 L120,44 L160,58 L200,46 L240,60 L270,50 L310,62 L350,48 L390,60 L430,50 L470,64 L510,52 L560,62 L600,50 L640,60 L690,48 L730,58 L770,46 L820,56 L860,44 L900,54 L950,42 L990,52 L1030,40 L1080,50 L1120,38 L1160,46 L1200,34 L1200,80 L0,80Z" fill="#fff"/>
</svg>

<section aria-labelledby="audience-title">
  <h2 id="audience-title" class="section-title abs" style="left:0;top:817px;width:1200px">Private Lessons and Group Classes<br>are Availiable for</h2>
  <div class="rule abs" style="left:572px;top:897px"></div>
  <div class="audience-circle" style="left:175px;top:982px;width:266px;height:292px">
    <svg width="72" height="68" viewBox="0 0 72 68" aria-hidden="true"><circle cx="21" cy="10" r="8" fill="#fff"/><circle cx="51" cy="10" r="8" fill="#fff"/><path d="M12 22h18l6 20h-7v24h-5V48h-2v18h-5V42H9z" fill="#fff"/><path d="M43 22h16l5 22h-5v22h-5V48h-2v18h-5V44h-5z" fill="#fff"/></svg>
    <span style="margin-top:12px">Children and<br>Teenagers</span>
  </div>
  <div class="audience-photo" role="img" aria-label="Smiling young people splashing together in an outdoor pool"><span>People with a Disability</span></div>
  <div class="audience-circle" style="left:758px;top:982px;width:266px;height:292px">
    <svg width="60" height="78" viewBox="0 0 60 78" aria-hidden="true"><circle cx="30" cy="18" r="16" fill="#fff"/><path d="M2 76c0-22 12-36 28-36s28 14 28 36z" fill="#fff"/></svg>
    <span style="margin-top:14px">Adults</span>
  </div>
</section>

<section aria-labelledby="about-title">
  <div class="about-bg" role="img" aria-label="Calm blue sea stretching to the horizon"></div>
  <div class="about-bar"></div>
  <div class="about-photo" role="img" aria-label="Swim instructor in a sun hat waving beside a smiling swimmer at a pool ladder"></div>
  <h2 id="about-title" class="h2 abs" style="left:657px;top:1440px">About Me</h2>
  <div class="rule abs" style="left:657px;top:1487px;width:62px"></div>
  <div class="abs" style="left:657px;top:1512px;width:417px">
    <p class="body-copy">Theo's life, from the very start, revolved around water. His parents met in a swimming club and started him swimming before he could walk! From a young age, teaching has come naturally to him and it is something that he truly enjoys.</p>
    <p class="body-copy" style="margin-top:26px">In his spare time, he enjoys hiking with friends and playing Ultimate Frisbee, including helping to coordinate a weekly social league.</p>
  </div>
  <a class="btn-blue btn" style="left:657px;top:1748px;width:167px">LEARN MORE
    <svg width="14" height="14" viewBox="0 0 14 14"><circle cx="7" cy="7" r="7" fill="#fff"/><path d="M4 7h5M7 4.5L9.5 7 7 9.5" stroke="#1a86c9" stroke-width="1.8" fill="none"/></svg>
  </a>
</section>
<svg class="abs" style="left:0;top:1890px" width="1200" height="70" viewBox="0 0 1200 70" aria-hidden="true">
  <path d="M0,20 L40,34 L80,26 L120,40 L170,30 L210,42 L260,32 L300,46 L350,36 L400,44 L450,34 L500,46 L560,38 L610,48 L660,36 L720,46 L770,34 L820,44 L870,32 L930,42 L980,30 L1030,40 L1080,28 L1130,38 L1200,24 L1200,70 L0,70Z" fill="#fff"/>
</svg>

<section aria-labelledby="loc-title">
  <h2 id="loc-title" class="h2 abs" style="left:110px;top:1998px">Locations</h2>
  <div class="rule abs" style="left:110px;top:2043px;width:62px"></div>
  <p class="body-copy abs" style="left:110px;top:2071px;width:459px;color:#333;font-size:14.5px">We'll do the travelling to where it is convenient for you.Current Council Areas Include: Campbelltown, Burnside, Unley, Prospect, Salisbury, Port Adelaide Enfield, Tea Tree Gully and Walkerville</p>
  <p class="abs" style="left:110px;top:2166px;font-size:14.5px;font-weight:500;color:var(--teal)">We teach in:</p>
  <ul class="check-list abs" style="left:110px;top:0">
    <li style="top:2206px"><svg width="14" height="14" viewBox="0 0 14 14"><circle cx="7" cy="7" r="7" fill="#1a86c9"/><path d="M3.8 7.2l2.2 2.2 4.2-4.4" stroke="#fff" stroke-width="1.8" fill="none"/></svg>Suitable Backyard Swimming Pools whether it's yours, a friend's or family members'.</li>
    <li style="top:2272px"><svg width="14" height="14" viewBox="0 0 14 14"><circle cx="7" cy="7" r="7" fill="#1a86c9"/><path d="M3.8 7.2l2.2 2.2 4.2-4.4" stroke="#fff" stroke-width="1.8" fill="none"/></svg>Private Hydrotherapy Pool at Klemzig</li>
    <li style="top:2306px"><svg width="14" height="14" viewBox="0 0 14 14"><circle cx="7" cy="7" r="7" fill="#1a86c9"/><path d="M3.8 7.2l2.2 2.2 4.2-4.4" stroke="#fff" stroke-width="1.8" fill="none"/></svg>Apartment Centre Pool where the client is a resident</li>
    <li style="top:2344px"><svg width="14" height="14" viewBox="0 0 14 14"><circle cx="7" cy="7" r="7" fill="#1a86c9"/><path d="M3.8 7.2l2.2 2.2 4.2-4.4" stroke="#fff" stroke-width="1.8" fill="none"/></svg>Other pools subject to negotiations with management.</li>
  </ul>
  <div class="dot-grid" aria-hidden="true"></div>
  <div class="abs" role="img" aria-label="Round above-ground backyard pool beside a wooden deck and flowering shrub" style="left:773px;top:2027px;width:319px;height:335px;background:linear-gradient(180deg,#4f7a3a 0%,#4a9bd6 45%,#8fb6cf 70%,#8a6a44 100%);box-shadow:0 6px 18px rgba(0,0,0,.18)"></div>
  <div class="abs" role="img" aria-label="Family of four standing together beside a backyard pool" style="left:608px;top:2132px;width:267px;height:296px;background:linear-gradient(180deg,#9ab5c4 0%,#58b8d0 45%,#d7c5b3 75%,#b8b0a8 100%);border:3px solid #fff;box-shadow:0 6px 18px rgba(0,0,0,.2)"></div>
</section>

<section aria-labelledby="why-title">
  <div class="why-band" role="img" aria-label="Rippling turquoise pool water"></div>
  <svg class="abs" style="left:0;top:2480px" width="1200" height="60" viewBox="0 0 1200 60" aria-hidden="true">
    <path d="M0,0 L1200,0 L1200,30 L1150,22 L1100,34 L1050,24 L1000,36 L950,26 L890,38 L840,28 L790,40 L730,30 L680,42 L630,32 L570,44 L520,34 L470,46 L420,34 L370,44 L320,32 L260,42 L210,30 L160,40 L110,28 L60,38 L0,26Z" fill="#fff"/>
  </svg>
  <svg class="abs" style="left:0;top:3120px" width="1200" height="70" viewBox="0 0 1200 70" aria-hidden="true">
    <path d="M0,24 L50,36 L100,26 L150,40 L210,30 L260,44 L320,32 L370,46 L430,34 L480,48 L540,36 L600,46 L650,34 L710,44 L770,32 L820,42 L880,30 L930,42 L990,28 L1040,38 L1100,26 L1150,36 L1200,22 L1200,70 L0,70Z" fill="#fff"/>
  </svg>
  <h2 id="why-title" class="abs" style="left:0;top:2630px;width:1200px;text-align:center;color:#fff;font-size:30px;font-weight:700">Why Theo and Yard Paddle?</h2>
  <div class="abs" style="left:568px;top:2675px;width:64px;height:4px;background:#fff;border-radius:2px"></div>
  <p class="abs" style="left:155px;top:2711px;width:890px;text-align:center;color:#fff;font-size:14.5px;line-height:26px">With over 10 years' experience teaching children, teenagers and adults, Theo brings the skills, knowledge, and passion to help swimmers of all ages and abilities achieve their goals. Yard Paddle offers a personalised approach to swimming lessons that can help individuals overcome their fears and technical challenges. The initial goal is to help the swimmer relax, feel comfortable and enjoy the water, from which all their other progress flows</p>

  <div class="why-feature" style="left:94px;top:2867px">
    <div class="why-icon"><svg width="52" height="60" viewBox="0 0 52 60" fill="none" stroke="#fff" stroke-width="2.6"><circle cx="26" cy="22" r="17"/><path d="M18 22l6 6 10-11"/><path d="M15 36l-6 20 9-4 5 7 3-12M37 36l6 20-9-4-5 7-3-12"/></svg></div>
    Experienced, Qualified and<br>Safety Cleared
  </div>
  <div class="why-feature" style="left:353px;top:2867px">
    <div class="why-icon"><svg width="58" height="56" viewBox="0 0 58 56" fill="#fff"><circle cx="29" cy="9" r="6"/><path d="M16 12l9 9h8l9-9 3 3-10 11v10H23V26L13 15z"/><circle cx="12" cy="32" r="5"/><circle cx="46" cy="32" r="5"/><rect x="6" y="39" width="12" height="15" rx="2"/><rect x="40" y="39" width="12" height="15" rx="2"/><rect x="23" y="39" width="12" height="15" rx="2"/></svg></div>
    Individual Approach
  </div>
  <div class="why-feature" style="left:608px;top:2867px">
    <div class="why-icon"><svg width="58" height="58" viewBox="0 0 58 58" fill="#fff"><path d="M29 3l14 5v11c0 10-6 16-14 19-8-3-14-9-14-19V8z"/><path d="M22 19l5 5 9-9" stroke="#4cc3ca" stroke-width="3" fill="none"/><circle cx="12" cy="42" r="5"/><circle cx="29" cy="44" r="5"/><circle cx="46" cy="42" r="5"/><path d="M4 56c0-6 4-8 8-8s8 2 8 8zM21 58c0-6 4-8 8-8s8 2 8 8zM38 56c0-6 4-8 8-8s8 2 8 8z"/></svg></div>
    Focus on both Technique<br>and Water Safety
  </div>
  <div class="why-feature" style="left:874px;top:2867px">
    <div class="why-icon"><svg width="54" height="58" viewBox="0 0 54 58" fill="none" stroke="#fff" stroke-width="2.6"><rect x="6" y="8" width="34" height="46" rx="3"/><rect x="15" y="3" width="16" height="8" rx="2" fill="#fff"/><path d="M12 22l3 3 5-5M12 34l3 3 5-5M24 23h10M24 35h6"/><path d="M48 18l-20 24-4 9 8-5 20-24z" fill="#fff"/></svg></div>
    Free home pool and swimmer<br>assessment
  </div>
</section>

<section aria-labelledby="book-title">
  <div class="abs" style="left:108px;top:3257px;width:441px;height:395px;background:#e8f1f7"></div>
  <div class="abs" role="img" aria-label="Two smiling girls in swim caps and goggles at the edge of a bright blue pool" style="left:128px;top:3240px;width:438px;height:393px;background:linear-gradient(180deg,#cfeefa 0%,#8fd5f2 35%,#3aa9e3 70%,#bfe4f4 100%)"></div>
  <h2 id="book-title" class="h2 abs" style="left:634px;top:3244px">Availability and Bookings</h2>
  <div class="rule abs" style="left:634px;top:3291px;width:62px"></div>
  <div class="abs" style="left:634px;top:3314px;width:458px;color:#333;font-size:14.5px;line-height:26px;text-align:justify">
    <p>We'll work with you to find a time and day that is suitable.</p>
    <p style="margin-top:12px">Use the message or calendar function icons on the right to leave your details, book a time for a chat or book in your FREE Home Pool and Swimmer Assessment.</p>
    <p style="margin-top:12px">We offer online payments and invoicing.</p>
    <p style="margin-top:12px">Generally, the season for home lessons in an outdoor backyard pool is November to April but we are flexible to work around your schedule and holidays.</p>
  </div>
  <a class="btn-blue btn" style="left:634px;top:3592px;width:166px">LEARN MORE
    <svg width="14" height="14" viewBox="0 0 14 14"><circle cx="7" cy="7" r="7" fill="#fff"/><path d="M4 7h5M7 4.5L9.5 7 7 9.5" stroke="#1a86c9" stroke-width="1.8" fill="none"/></svg>
  </a>
</section>

<svg class="abs" style="left:0;top:3715px" width="1200" height="70" viewBox="0 0 1200 70" aria-hidden="true">
  <path d="M0,40 L30,30 L70,44 L110,28 L150,40 L190,24 L240,38 L280,26 L330,42 L370,22 L420,36 L460,26 L510,40 L560,24 L600,36 L650,28 L690,40 L740,22 L790,38 L830,26 L880,40 L930,24 L970,36 L1020,26 L1070,40 L1110,28 L1160,38 L1200,26 L1200,70 L0,70Z" fill="#121212"/>
</svg>
<footer class="site-footer">
  <div class="abs" style="left:106px;top:175px;width:205px;text-align:center">
    <span class="brand-name" style="font-size:30px">YARDPADDLE</span>
  </div>

  <h3 class="foot-h" style="left:397px;top:92px">Quick Links</h3>
  <nav class="foot-links" aria-label="Footer">
    <a style="left:397px;top:140px">Home</a>
    <a style="left:397px;top:171px">About Me</a>
    <a style="left:397px;top:202px">My services</a>
    <a style="left:397px;top:233px">Testimonies</a>
    <a style="left:397px;top:264px">Pricing</a>
    <a style="left:397px;top:295px">Links</a>
  </nav>

  <h3 class="foot-h" style="left:585px;top:92px">Contact Us</h3>
  <div class="contact-row" style="left:585px;top:144px"><span class="contact-ico"><svg width="12" height="12" viewBox="0 0 12 12"><path d="M2.5 1l2 2.5-1 1.3a7 7 0 0 0 3.7 3.7l1.3-1 2.5 2-1 1.5C6 11 1 6 1 2z" fill="#fff"/></svg></span>+1 555 014 2290</div>
  <div class="contact-row" style="left:585px;top:195px"><span class="contact-ico"><svg width="12" height="10" viewBox="0 0 12 10"><rect x=".5" y=".5" width="11" height="9" fill="#fff"/><path d="M.5 .5L6 5l5.5-4.5" stroke="#3a3a3a" fill="none"/></svg></span>info@yardpaddle.net</div>
  <div class="contact-row" style="left:585px;top:246px"><span class="contact-ico"><svg width="10" height="13" viewBox="0 0 10 13"><path d="M5 0a5 5 0 0 1 5 5c0 3-5 8-5 8S0 8 0 5a5 5 0 0 1 5-5z" fill="#fff"/><circle cx="5" cy="5" r="1.8" fill="#3a3a3a"/></svg></span>12, Loremed consectetur</div>
  <div class="contact-row" style="left:585px;top:297px"><span class="contact-ico"><svg width="12" height="12" viewBox="0 0 12 12" fill="none" stroke="#fff" stroke-width="1.2"><circle cx="6" cy="6" r="5"/><ellipse cx="6" cy="6" rx="2.2" ry="5"/><path d="M1 6h10"/></svg></span>www.yardpaddle.net</div>

  <h3 class="foot-h" style="left:867px;top:92px">Subscribe To Newsletter</h3>
  <p class="abs" style="left:867px;top:140px;width:240px;font-size:11.5px;line-height:20px">Sign up today to get resources on how to attract and retain more customers!</p>
  <div class="abs" style="left:867px;top:198px;width:235px;height:34px;background:#fff;border-radius:17px 0 0 17px;font-size:10.5px;color:#888;display:flex;align-items:center;padding-left:16px;gap:6px">
    <svg width="10" height="8" viewBox="0 0 10 8"><rect x=".5" y=".5" width="9" height="7" fill="none" stroke="#888"/></svg>Email Address
  </div>
  <div class="abs" style="left:1054px;top:198px;width:48px;height:34px;background:var(--teal);border-radius:0 17px 17px 0;display:flex;align-items:center;justify-content:center">
    <svg width="15" height="15" viewBox="0 0 15 15"><path d="M14 1L1 7l5 2 2 5z" fill="#fff"/></svg>
  </div>
  <span class="social" style="left:867px;top:253px" aria-label="Social profile"></span>
  <span class="social" style="left:905px;top:253px" aria-label="Social profile"></span>
  <span class="social" style="left:943px;top:253px" aria-label="Social profile"></span>
  <span class="social" style="left:981px;top:253px" aria-label="Social profile"></span>

  <span class="abs" style="left:1131px;top:307px;width:40px;height:40px;border-radius:50%;background:var(--teal);display:flex;align-items:center;justify-content:center" aria-label="Chat">
    <svg width="20" height="18" viewBox="0 0 20 18"><path d="M10 1C4.8 1 1 4.3 1 8.2c0 2 1 3.8 2.6 5L3 17l4.2-2.2c.9.3 1.8.4 2.8.4 5.2 0 9-3.3 9-7S15.2 1 10 1z" fill="#fff"/><circle cx="6.5" cy="8.2" r="1.2" fill="#17a493"/><circle cx="10" cy="8.2" r="1.2" fill="#17a493"/><circle cx="13.5" cy="8.2" r="1.2" fill="#17a493"/></svg>
  </span>
</footer>

<div class="legal-bar">
  <p class="abs" style="left:113px;top:21px">Copyright© 2022 <u>Yard paddle</u> | All Rights Reserved</p>
  <p class="abs" style="left:786px;top:21px;white-space:nowrap">Terms &amp; Condition &nbsp; | &nbsp; Site Map &nbsp; | &nbsp; Privacy Policy</p>
</div>

</body>
</html>
```